Business Card Design for Software Development Company

I am looking for a business card design the incorporates my new logo (attached below).

Key information to include:
Name: Darnell Whisket
Title: CEO
Email: darnell@brovatecore.com
Phone: 418-926-7301
Website: www.brovatecore.com

NOTE: This design should be easy to edit so that we can order cards for different members of our team.

```html
<!DOCTYPE html>
<html lang="en">
<head>
<meta charset="utf-8">
<title>Brovate Core — Business Card</title>
<link href="https://fonts.googleapis.com/css2?family=Montserrat:wght@400;500;700&display=swap" rel="stylesheet">
<style>
  :root {
    --backdrop: #959595;
    --navy: #373e56;
    --white: #ffffff;
    --accent: #e9782a;
    --ink: #2f3650;
  }
  * { margin: 0; padding: 0; box-sizing: border-box; }
  html, body {
    width: 1200px; height: 1108px; overflow: hidden;
    background: var(--backdrop);
    font-family: "Montserrat", Arial, sans-serif;
  }
  .canvas { position: relative; width: 1200px; height: 1108px; }
  .card {
    position: absolute; left: 241px; width: 741px; height: 423px;
    border-radius: 32px; overflow: hidden;
  }
  .card--front { top: 117px; background: var(--navy); }
  .card--back { top: 578px; background: var(--white); }

  .brand {
    position: absolute; display: flex; flex-direction: column; align-items: flex-end;
  }
  .brand__row { display: flex; align-items: center; gap: 14px; }
  .brand__mark { background: var(--accent); flex: none; }
  .brand__name { font-weight: 700; letter-spacing: -1px; line-height: 1; }
  .brand__tagline { font-weight: 700; letter-spacing: 0.4px; }

  .card--front .brand { left: 70px; top: 170px; width: 600px; }
  .card--front .brand__mark { width: 34px; height: 34px; }
  .card--front .brand__name { color: var(--white); font-size: 70px; }
  .card--front .brand__tagline { color: var(--white); font-size: 9.5px; margin-top: 8px; }

  .card--back .brand { left: 30px; top: 226px; width: 292px; }
  .card--back .brand__mark { width: 20px; height: 20px; }
  .card--back .brand__name { color: var(--navy); font-size: 38px; }
  .card--back .brand__tagline { color: var(--navy); font-size: 5.5px; margin-top: 4px; }

  .divider {
    position: absolute; left: 350px; top: 122px; width: 2px; height: 178px;
    background: linear-gradient(var(--white), var(--navy) 20%, var(--navy) 80%, var(--white));
  }
  .person { position: absolute; left: 384px; top: 126px; color: var(--ink); }
  .person__name { font-size: 29px; font-weight: 700; line-height: 1.1; }
  .person__title { font-size: 20px; font-weight: 400; margin-top: 6px; }

  .contacts { position: absolute; left: 377px; top: 206px; list-style: none; }
  .contacts__item {
    display: flex; align-items: center; height: 29.5px;
    font-size: 20px; color: var(--ink); letter-spacing: 0.3px;
  }
  .contacts__icon { width: 22px; height: 22px; margin-right: 11px; fill: var(--navy); flex: none; }
</style>
</head>
<body>
<main class="canvas">
  <section class="card card--front" aria-label="Card front">
    <div class="brand">
      <div class="brand__row">
        <span class="brand__mark"></span>
        <span class="brand__name">Brovate Core</span>
      </div>
      <span class="brand__tagline">A DIVISION OF BROVATE GROUP</span>
    </div>
  </section>

  <section class="card card--back" aria-label="Card back">
    <div class="brand">
      <div class="brand__row">
        <span class="brand__mark"></span>
        <span class="brand__name">Brovate Core</span>
      </div>
      <span class="brand__tagline">A DIVISION OF BROVATE GROUP</span>
    </div>

    <div class="divider"></div>

    <div class="person">
      <p class="person__name">Darnell Whisket</p>
      <p class="person__title">CEO</p>
    </div>

    <ul class="contacts">
      <li class="contacts__item">
        <svg class="contacts__icon" viewBox="0 0 24 24" aria-hidden="true"><path d="M6.6 10.8a15.1 15.1 0 0 0 6.6 6.6l2.2-2.2a1 1 0 0 1 1-.25 11.4 11.4 0 0 0 3.6.57 1 1 0 0 1 1 1V20a1 1 0 0 1-1 1A17 17 0 0 1 3 4a1 1 0 0 1 1-1h3.5a1 1 0 0 1 1 1c0 1.25.2 2.45.57 3.6a1 1 0 0 1-.25 1z"/></svg>
        418-926-7301
      </li>
      <li class="contacts__item">
        <svg class="contacts__icon" viewBox="0 0 24 24" aria-hidden="true"><path d="M2 5h20v2.2l-10 6.3L2 7.2z M2 9.6l10 6.3 10-6.3V19H2z"/></svg>
        darnell@brovatecore.com
      </li>
      <li class="contacts__item">
        <svg class="contacts__icon" viewBox="0 0 24 24" aria-hidden="true"><circle cx="12" cy="12" r="10"/><path d="M7 6c2 0 3 1.5 2.5 3S7 10 6.5 12 8 15 9 17l-1 3 M15 4c-1 2 0 3 2 3.5s2 3 1 4.5-2 2-2 4 1 2.5 1 2.5" stroke="#fff" stroke-width="1.6" fill="none"/></svg>
        www.brovatecore.com
      </li>
    </ul>
  </section>
</main>
</body>
</html>
```